tiling company needs letterhead urgent

We need a logo to represent our company on an electronic letterhead. We are a tiling firm called Corliss Flooring Ltd and undertake all aspects of tiling work. The final design of the logo should incorporate the type of work we do and should be modern. We do not want any designs which may be considered 'novelty' or 'cartoonish.' No characters please, we require something sleek and contemporary . Please ensure the company name is central to your design ,Corliss Flooring Ltd

Industry/Entity Type

Electronic

Requirements
Must have
• text on letterhead to included

Registered address 58 Brindle grove Hapton Manchester M629QT
Company number 5273908
VAT no 741596238
Mobile no 07812649375
Office no 0161 548 7013
Web :www.surfacecraftexample.co.uk
Email : gerald@surfacecraftexample.co.uk
Nice to have
• a tile theme

```html
<!DOCTYPE html>
<html lang="en">
<head>
<meta charset="utf-8">
<title>Corliss Flooring Ltd – Letterhead</title>
<link rel="stylesheet" href="https://fonts.googleapis.com/css2?family=Arimo:wght@400&family=Dosis:wght@400;500&display=swap">
<style>
  :root {
    --header-dark: #262626;
    --brand-green: #2db83d;
    --paper: #ffffff;
    --ink: #222222;
    --on-dark: #ffffff;
  }
  html, body {
    margin: 0;
    padding: 0;
    overflow: hidden;
    background: var(--paper);
  }
  .letterhead {
    position: relative;
    width: 848px;
    height: 1200px;
    overflow: hidden;
    background: var(--paper);
    font-family: "Arimo", Arial, sans-serif;
    color: var(--ink);
  }
  .header-shapes {
    position: absolute;
    inset: 0 0 auto 0;
    width: 848px;
    height: 300px;
  }
  .brand {
    position: absolute;
    left: 24px;
    top: 70px;
    display: flex;
    align-items: center;
    gap: 12px;
  }
  .brand-mark {
    width: 22px;
    height: 22px;
    background: var(--brand-green);
  }
  .brand-name {
    font-family: "Dosis", Arial, sans-serif;
    font-weight: 500;
    font-size: 28px;
    color: var(--on-dark);
    letter-spacing: 0.2px;
  }
  .company-details {
    position: absolute;
    right: 20px;
    top: 12px;
    margin: 0;
    text-align: right;
    font-family: "Dosis", Arial, sans-serif;
    font-size: 16px;
    line-height: 20px;
    color: var(--on-dark);
    font-style: normal;
  }
  .letter-body {
    position: absolute;
    left: 40px;
    top: 172px;
    width: 764px;
    font-size: 15.8px;
    line-height: 21px;
  }
  .letter-body p {
    margin: 0 0 20px;
  }
  .letter-body .salutation {
    margin-bottom: 28px;
  }
  .letter-body .sign-off {
    margin-top: 34px;
    margin-bottom: 28px;
  }
  .footer-band {
    position: absolute;
    left: 0;
    bottom: 0;
    width: 848px;
    height: 34px;
    background: var(--brand-green);
  }
</style>
</head>
<body>
<div class="letterhead">
  <svg class="header-shapes" viewBox="0 0 848 300" aria-hidden="true">
    <rect x="0" y="0" width="848" height="124" fill="var(--header-dark)"/>
    <polygon points="470,0 848,0 848,290 530,124 520,110" fill="var(--brand-green)"/>
  </svg>

  <div class="brand">
    <span class="brand-mark"></span>
    <span class="brand-name">Corliss Flooring Ltd.</span>
  </div>

  <address class="company-details">
    58 Brindle grove, Hapton<br>
    Manchester, M629QT<br>
    Company number 5273908<br>
    VAT no 741596238<br>
    Mobile 07812649375<br>
    Office 0161 548 7013<br>
    gerald@surfacecraftexample.co.uk<br>
    www.surfacecraftexample.co.uk
  </address>

  <main class="letter-body">
    <p class="salutation">Dear Ms. Harrow:</p>
    <p>I am writing to ask if you would pass along a request to Dana Whitlock.</p>
    <p>Two years ago, I had hit "rock bottom"-- I was agoraphobic, and had been unable to leave my house for more than a year. Prior to that time, I was a stage actress with aspirations to move to L.A. and start a film career. Panic disorder erased that dream for me, and I had given up on life.</p>
    <p>About this time, I saw the NorthLight TV documentary "Still Waters," and was floored when I heard Ms. Whitlock discussing the very same experiences I'd been having. I am so thankful for her honesty and grateful for the hope she gave me. After watching the show, I didn't feel so crazy, after all. It was so inspiring for me to find out that someone who'd been as low as I was had battled this disorder and fought so hard to keep her dreams alive.</p>
    <p>The worst parts of this disorder were the loneliness and hopelessness, and it was easy to feel like no one else in the world had ever gone through what I had and managed to live a successful life. I promised myself that if I ever overcame agoraphobia, I would remember to pass on that hope to others. That day has finally come, and I'm keeping that promise.</p>
    <p>I have compiled an anthology of success stories from people who have overcome all sorts of anxiety disorders. There are 33 stories in total, from people all over the world, and Dr. Alan Preece (author of Steady Ground) has provided commentaries about each of the stories. The book, Beyond the Quiet Fear, is under contract and will be published in paperback and hardcover by Larkfield Press in fall, 2002.</p>
    <p>I am writing to ask if Ms. Whitlock might be interested in reading the book and possibly writing a short blurb for its cover. I know she has a very busy schedule, but I'm hoping that she shares my desire to help people who are still suffering as we were. I would be happy to send the manuscript for her consideration, and provide any background information she'd like.</p>
    <p>Thank you very much for taking the time to read this. Please feel free to contact me anytime by phone or e-mail. I look forward to your response.</p>
    <p class="sign-off">Regards,</p>
    <p>Nora Pellham</p>
  </main>

  <div class="footer-band"></div>
</div>
</body>
</html>
```